BriarLoom Website Homepage Design

Please provide your idea of homepage for a hosting company. This project is for DESIGN only, no coding.

It must use/combine colors used in logo, clean, modern look.

Homepage must consist of at least 4 sections (example: testimonials, services, and so on. not necesarily all of them). We would like the navigation to be horizontal, but not mandatory.

You can include a preview of services page (optional, not a must).

Number of Pages Required

1 page

Font styles to use
Sans Serif

```html
<!DOCTYPE html>
<html lang="en">
<head>
<meta charset="utf-8">
<title>BriarLoom – Web Hosting</title>
<link href="https://fonts.googleapis.com/css2?family=Roboto:ital,wght@0,300;0,400;0,500;0,700;0,900;1,400&display=swap" rel="stylesheet">
<style>
:root{
  --blue:#0a7fd8;
  --blue-dark:#0669b8;
  --ink:#1d1d1d;
  --grey:#6d6d6d;
  --grey-light:#9a9a9a;
  --card-grey:#9b9b9b;
  --btn-dark:#4a4a4a;
  --pale:#e4f1fc;
  --line:#e3e3e3;
  --footer:#3c3c3c;
  --white:#fff;
}
*{margin:0;padding:0;box-sizing:border-box}
html,body{width:1200px;height:4227px;overflow:hidden}
body{font-family:'Roboto',sans-serif;color:var(--ink);background:var(--white);position:relative}
.abs{position:absolute}
.section-title{position:absolute;left:0;width:1200px;text-align:center;font-size:34px;font-weight:900;color:var(--blue);letter-spacing:.5px;text-transform:uppercase;line-height:1}
.section-title span{font-weight:300;color:var(--grey-light)}
.rule{position:absolute;height:3px;width:32px;background:var(--blue)}

/* nav */
.nav{top:0;left:0;width:1200px;height:66px}
.brand{left:102px;top:17px;font-size:28px;font-weight:500;color:var(--blue);letter-spacing:1px}
.menu{left:343px;top:26px;display:flex;gap:27px;font-size:12.5px;font-weight:700;text-transform:uppercase}
.menu a{color:var(--ink);text-decoration:none}
.menu a.active{color:var(--blue)}
.login{left:998px;top:16px;width:100px;height:36px;background:var(--blue);color:#fff;border-radius:3px;font-size:13px;font-weight:700;display:flex;align-items:center;justify-content:center;gap:7px}

/* hero */
.hero{top:66px;left:0;width:1200px;height:660px}
.hero-photo{position:absolute;inset:0;background:linear-gradient(100deg,#5f6f86 0%,#2f4462 30%,#14253f 60%,#0d1a2e 100%)}
.hero-title{left:624px;top:150px;font-size:66px;font-weight:900;color:#fff;letter-spacing:1px}
.hero-text{left:625px;top:236px;width:480px;font-size:14.5px;line-height:25px;color:#fff}
.hero-btn{left:625px;top:310px;width:163px;height:46px;background:var(--blue);color:#fff;border-radius:3px;font-size:13.5px;font-weight:700;display:flex;align-items:center;justify-content:center;gap:8px}
.dots{left:572px;top:472px;display:flex;gap:4px}
.dots i{width:9px;height:9px;border-radius:50%;background:#fff;display:block}
.dots i.off{background:none;border:1.5px solid #fff}

/* about */
.about-title{left:148px;top:800px;font-size:34px;font-weight:900;color:var(--blue)}
.about-title span{font-weight:300;color:var(--grey-light)}
.about-text{left:148px;top:870px;width:427px;font-size:13.5px;line-height:25.7px;color:var(--grey);text-align:justify}
.btn{position:absolute;background:var(--blue);color:#fff;border-radius:3px;font-size:13.5px;font-weight:700;display:flex;align-items:center;justify-content:center;gap:8px;text-transform:uppercase}
.about-photo{left:647px;top:783px;width:404px;height:404px;border-radius:50%;background:radial-gradient(circle at 50% 55%,#8cc0ff 0%,#3c74e6 35%,#1a3a9c 70%,#0e1f5e 100%)}

/* services */
.services{top:1292px;left:0;width:1200px;height:793px;background:var(--pale)}
.svc-grid{left:107px;top:200px;width:988px;height:600px}
.svc{position:absolute;width:330px;text-align:center}
.svc .icon{width:112px;height:112px;border-radius:50%;background:var(--blue);margin:0 auto;display:flex;align-items:center;justify-content:center}
.svc h3{margin-top:27px;font-size:14px;font-weight:700;text-transform:uppercase;color:#111}
.svc .bar{width:32px;height:3px;background:var(--blue);margin:13px auto 12px}
.svc p{font-size:13.5px;line-height:21.5px;color:var(--grey);width:280px;margin:0 auto}
.vline{position:absolute;width:1px;background:#cfe0ee}
.hline{position:absolute;height:1px;background:#cfe0ee}

/* pricing */
.plan{position:absolute;top:2275px;width:317px;height:535px;border:1px solid var(--line);text-align:center}
.plan.featured{border:2px solid var(--blue)}
.plan .head{position:absolute;left:10px;right:10px;top:9px;height:55px;background:var(--card-grey);color:#fff;font-size:15px;font-weight:700;text-transform:uppercase;padding-top:30px}
.plan.featured .head{background:var(--blue)}
.plan .head::before{content:"";position:absolute;left:50%;top:13px;width:34px;height:2px;margin-left:-17px;background:#fff}
.plan .from{position:absolute;left:0;width:100%;top:90px;font-size:13px;font-weight:700}
.plan .price{position:absolute;left:0;width:100%;top:110px;font-size:38px;font-weight:700;color:var(--card-grey)}
.plan.featured .price{color:var(--blue)}
.plan .per{position:absolute;left:0;width:100%;top:161px;font-size:13px;font-weight:700}
.plan .offer{position:absolute;left:55px;width:207px;top:191px;height:42px;background:var(--btn-dark);color:#fff;font-size:13px;font-weight:700;display:flex;align-items:center;justify-content:center}
.plan .intro{position:absolute;left:27px;width:270px;top:270px;text-align:left;font-size:13.5px;line-height:20px;color:var(--grey)}
.plan ul{position:absolute;left:27px;top:327px;list-style:none;text-align:left}
.plan li{font-size:13.5px;color:var(--grey);height:27.3px;display:flex;align-items:center;gap:10px}
.plan li svg{flex:none}
.plan .cta{left:22px;width:272px;top:475px;height:46px;background:var(--card-grey);font-size:13px}
.plan.featured .cta{background:var(--blue);left:21px}

/* testimonials */
.testimonials{top:2927px;left:0;width:1200px;height:448px;background:linear-gradient(135deg,#1a8ee6 0%,#0a7bd3 50%,#0668bb 100%)}
.quote{position:absolute;top:169px;width:467px;height:207px;background:#fff}
.avatar{position:absolute;left:17px;top:20px;width:72px;height:72px;border-radius:50%;background:linear-gradient(#cfd7df,#8b98a6);border:3px solid #dce9f5}
.quote .nbar{position:absolute;left:119px;top:43px;width:34px;height:2px;background:var(--blue)}
.quote .name{position:absolute;left:119px;top:53px;font-size:13px;color:#111}
.quote .name b{font-weight:700}
.quote .name span{color:var(--grey)}
.quote p{position:absolute;left:22px;top:111px;width:425px;font-size:12.5px;line-height:21px;font-style:italic;color:var(--grey)}
.stars{position:absolute;right:32px;top:160px;display:flex;gap:2px}
.arrow{position:absolute;top:262px}

/* why */
.why{position:absolute;top:3567px;width:237px;height:246px;border:1px solid var(--line);text-align:center}
.why .ic{width:68px;height:68px;border-radius:50%;background:#8a8a8a;margin:27px auto 0;display:flex;align-items:center;justify-content:center}
.why h4{margin-top:36px;font-size:12.5px;font-weight:700;text-transform:uppercase}
.why p{margin:12px auto 0;width:205px;font-size:13.5px;line-height:21.5px;color:var(--grey)}

/* footer */
.footer{top:3931px;left:0;width:1200px;height:296px;background:var(--footer);color:#fff}
.socials{left:0;width:1200px;top:53px;display:flex;justify-content:center;gap:17px}
.socials i{display:block;width:40px;height:40px;border:2px solid #fff;border-radius:50%}
.contact{left:0;width:1200px;top:128px;display:flex;justify-content:center;align-items:center;font-size:13.5px}
.contact .item{display:flex;align-items:center;gap:11px;padding:0 24px}
.contact .sep{width:1px;height:18px;background:#fff}
.fmenu{left:0;width:1200px;top:185px;display:flex;justify-content:center;gap:27px;font-size:12.5px;font-weight:700;text-transform:uppercase}
.copy{left:0;width:1200px;top:232px;text-align:center;font-size:13.5px}
</style>
</head>
<body>

<!-- navigation -->
<header class="nav abs">
  <div class="brand abs">BriarLoom</div>
  <nav class="menu abs">
    <a class="active">Home</a><a>About Us</a><a>Our Services</a><a>Features</a><a>Pricing</a><a>Reviews</a><a>Contact Us</a>
  </nav>
  <div class="login abs">LOG IN
    <svg width="10" height="12" viewBox="0 0 10 12"><rect x="1" y="5" width="8" height="7" rx="1" fill="#fff"/><path d="M3 5V3.5a2 2 0 0 1 4 0V5" stroke="#fff" stroke-width="1.6" fill="none"/></svg>
  </div>
</header>

<!-- hero -->
<section class="hero abs">
  <div class="hero-photo" role="img" aria-label="Technician holding a laptop in a data centre aisle of server racks"></div>
  <h1 class="hero-title abs">BRIARLOOM</h1>
  <p class="hero-text abs">Lorem ipsum dolor sit amet, consectetur adipiscing elit, sed do eiusmod tempor incididunt ut labore et dolore magna aliqua.</p>
  <div class="hero-btn abs">EXPLORE MORE
    <svg width="14" height="14" viewBox="0 0 14 14"><circle cx="7" cy="7" r="7" fill="#fff"/><path d="M5.5 4l3 3-3 3" stroke="#0a7fd8" stroke-width="2" fill="none"/></svg>
  </div>
  <div class="dots abs"><i></i><i></i><i class="off"></i><i></i><i></i></div>
  <svg class="abs" style="left:0;top:0" width="1200" height="660" viewBox="0 66 1200 660">
    <path d="M0 563 L600 672 L1200 563 L1200 726 L0 726 Z" fill="#fff"/>
    <path d="M120 588 L600 676 L1080 588 L600 690 Z" fill="#0a7fd8"/>
    <circle cx="600" cy="681" r="22" fill="#0a7fd8" stroke="#fff" stroke-width="4"/>
    <g fill="#fff"><rect x="590" y="671" width="20" height="5" rx="1"/><rect x="590" y="678" width="20" height="5" rx="1"/><rect x="590" y="685" width="20" height="5" rx="1"/></g>
  </svg>
</section>

<!-- about -->
<h2 class="about-title abs">ABOUT <span>US</span></h2>
<div class="rule" style="left:148px;top:849px"></div>
<p class="about-text abs">Sed ut perspiciatis unde omnis iste natus error sit volup accusantium doloremque laudantium, totam rem aperiam, eaque ipsa quae inventore veritatis et quasi architecto beatae vitae dicta sunt explicabo. Nenim ipsam voluptatem quia voluptas sit aspernatur aut odit aut fugit, sed quia consequuntur magni dolores eos qui ratione voluptatem nesciunt. Neque porro quisquam est, qui dolorem ipsum quia dolor consectetur, adipisci velit, sed quia non numquam eius modi tempora incidunt ut labore et dolore magnam aliquam quaerat voluptatem.</p>
<div class="btn" style="left:149px;top:1121px;width:145px;height:45px">Learn More
  <svg width="14" height="14" viewBox="0 0 14 14"><circle cx="7" cy="7" r="7" fill="#fff"/><path d="M5.5 4l3 3-3 3" stroke="#0a7fd8" stroke-width="2" fill="none"/></svg>
</div>
<div class="about-photo abs" role="img" aria-label="Blue-lit server room corridor seen through a circular frame"></div>

<!-- services -->
<section class="services abs">
  <h2 class="section-title" style="top:80px">OUR <span>SERVICES</span></h2>
  <div class="rule" style="left:584px;top:132px"></div>
  <div class="vline" style="left:430px;top:200px;height:530px"></div>
  <div class="vline" style="left:773px;top:200px;height:530px"></div>
  <div class="hline" style="left:107px;top:451px;width:989px"></div>

  <div class="svc" style="left:86px;top:180px">
    <div class="icon"><svg width="60" height="60" viewBox="0 0 60 60" fill="#fff"><path d="M16 26a14 12 0 0 1 27-3 9 9 0 0 1 1 17H17a8 8 0 0 1-1-14z"/><rect x="14" y="34" width="32" height="8" rx="2" fill="#0a7fd8" stroke="#fff" stroke-width="2"/><rect x="14" y="44" width="32" height="8" rx="2"/></svg></div>
    <h3>Web Hosting</h3><div class="bar"></div>
    <p>Lorem ipsum dolor sit amet, consec tetur adipiscing elit, sed do eiusmotempor incididunt ut labore et dolor</p>
  </div>
  <div class="svc" style="left:434px;top:180px">
    <div class="icon"><svg width="60" height="60" viewBox="0 0 60 60" fill="#fff"><rect x="12" y="12" width="30" height="9" rx="1"/><rect x="12" y="24" width="30" height="9" rx="1"/><rect x="12" y="36" width="24" height="9" rx="1"/><path d="M44 34l8 3v6c0 5-4 8-8 9-4-1-8-4-8-9v-6z"/></svg></div>
    <h3>Wordpress Hosting</h3><div class="bar"></div>
    <p>Lorem ipsum dolor sit amet, consec tetur adipiscing elit, sed do eiusmotempor incididunt ut labore et dolor</p>
  </div>
  <div class="svc" style="left:782px;top:180px">
    <div class="icon"><svg width="60" height="60" viewBox="0 0 60 60" fill="#fff"><rect x="13" y="12" width="34" height="9" rx="2"/><rect x="13" y="24" width="34" height="9" rx="2"/><path d="M22 48a7 7 0 0 1 3-13 9 9 0 0 1 17 2 6 6 0 0 1 0 11z"/></svg></div>
    <h3>VPS Hosting</h3><div class="bar"></div>
    <p>Lorem ipsum dolor sit amet, consec tetur adipiscing elit, sed do eiusmotempor incididunt ut labore et dolor</p>
  </div>
  <div class="svc" style="left:86px;top:484px">
    <div class="icon"><svg width="60" height="60" viewBox="0 0 60 60" fill="#fff"><rect x="14" y="12" width="32" height="10" rx="3"/><rect x="14" y="25" width="32" height="10" rx="3"/><rect x="14" y="38" width="32" height="10" rx="3"/></svg></div>
    <h3>Dedicated Servers</h3><div class="bar"></div>
    <p>Lorem ipsum dolor sit amet, consec tetur adipiscing elit, sed do eiusmotempor incididunt ut labore et dolor</p>
  </div>
  <div class="svc" style="left:434px;top:484px">
    <div class="icon"><svg width="60" height="60" viewBox="0 0 60 60"><circle cx="30" cy="26" r="13" fill="none" stroke="#fff" stroke-width="4"/><path d="M22 37l-6 12 6-1 3 5 5-11zM38 37l6 12-6-1-3 5-5-11z" fill="#fff"/></svg></div>
    <h3>SSL Certificates</h3><div class="bar"></div>
    <p>Lorem ipsum dolor sit amet, consec tetur adipiscing elit, sed do eiusmotempor incididunt ut labore et dolor</p>
  </div>
  <div class="svc" style="left:782px;top:484px">
    <div class="icon"><svg width="60" height="60" viewBox="0 0 60 60" fill="#fff"><rect x="16" y="12" width="30" height="9" rx="2"/><rect x="12" y="25" width="36" height="9" rx="2"/><rect x="16" y="38" width="30" height="9" rx="2"/></svg></div>
    <h3>Ecommerce Hosting</h3><div class="bar"></div>
    <p>Lorem ipsum dolor sit amet, consec tetur adipiscing elit, sed do eiusmotempor incididunt ut labore et dolor</p>
  </div>
</section>

<!-- pricing -->
<h2 class="section-title" style="top:2176px">CHOOSE <span>YOUR PRICING</span></h2>
<div class="rule" style="left:584px;top:2228px"></div>

<div class="plan" style="left:107px">
  <div class="head">Web Hosting</div>
  <div class="from">STARTING FROM</div><div class="price">$3.95</div><div class="per">PER MONTH</div>
  <div class="offer">FIRST 30 DAYS ONLY $1</div>
  <p class="intro">Lorem ipsum dolor sit amet, consectetur adipiscing</p>
  <ul>
    <li><svg width="13" height="13" viewBox="0 0 14 14"><circle cx="7" cy="7" r="7" fill="#9b9b9b"/><path d="M5.5 4l3 3-3 3" stroke="#fff" stroke-width="2" fill="none"/></svg>Sed ut perspiciatis unde omnis iste</li>
    <li><svg width="13" height="13" viewBox="0 0 14 14"><circle cx="7" cy="7" r="7" fill="#9b9b9b"/><path d="M5.5 4l3 3-3 3" stroke="#fff" stroke-width="2" fill="none"/></svg>Sed ut perspiciatis unde omnis iste</li>
    <li><svg width="13" height="13" viewBox="0 0 14 14"><circle cx="7" cy="7" r="7" fill="#9b9b9b"/><path d="M5.5 4l3 3-3 3" stroke="#fff" stroke-width="2" fill="none"/></svg>Sed ut perspiciatis unde omnis iste</li>
    <li><svg width="13" height="13" viewBox="0 0 14 14"><circle cx="7" cy="7" r="7" fill="#9b9b9b"/><path d="M5.5 4l3 3-3 3" stroke="#fff" stroke-width="2" fill="none"/></svg>Sed ut perspiciatis unde omnis iste</li>
  </ul>
  <div class="btn cta">View Web Hosting Plan</div>
</div>

<div class="plan featured" style="left:443px">
  <div class="head">Reseller Hosting</div>
  <div class="from">STARTING FROM</div><div class="price">$3.95</div><div class="per">PER MONTH</div>
  <div class="offer">FIRST 30 DAYS ONLY $1</div>
  <p class="intro">Lorem ipsum dolor sit amet, consectetur adipiscing</p>
  <ul>
    <li><svg width="13" height="13" viewBox="0 0 14 14"><circle cx="7" cy="7" r="7" fill="#0a7fd8"/><path d="M5.5 4l3 3-3 3" stroke="#fff" stroke-width="2" fill="none"/></svg>Sed ut perspiciatis unde omnis iste</li>
    <li><svg width="13" height="13" viewBox="0 0 14 14"><circle cx="7" cy="7" r="7" fill="#0a7fd8"/><path d="M5.5 4l3 3-3 3" stroke="#fff" stroke-width="2" fill="none"/></svg>Sed ut perspiciatis unde omnis iste</li>
    <li><svg width="13" height="13" viewBox="0 0 14 14"><circle cx="7" cy="7" r="7" fill="#0a7fd8"/><path d="M5.5 4l3 3-3 3" stroke="#fff" stroke-width="2" fill="none"/></svg>Sed ut perspiciatis unde omnis iste</li>
    <li><svg width="13" height="13" viewBox="0 0 14 14"><circle cx="7" cy="7" r="7" fill="#0a7fd8"/><path d="M5.5 4l3 3-3 3" stroke="#fff" stroke-width="2" fill="none"/></svg>Sed ut perspiciatis unde omnis iste</li>
  </ul>
  <div class="btn cta">View Web Hosting Plan</div>
</div>

<div class="plan" style="left:776px">
  <div class="head">Virtual Private Servers</div>
  <div class="from">STARTING FROM</div><div class="price">$3.95</div><div class="per">PER MONTH</div>
  <div class="offer">FIRST 30 DAYS ONLY $1</div>
  <p class="intro">Lorem ipsum dolor sit amet, consectetur adipiscing</p>
  <ul>
    <li><svg width="13" height="13" viewBox="0 0 14 14"><circle cx="7" cy="7" r="7" fill="#9b9b9b"/><path d="M5.5 4l3 3-3 3" stroke="#fff" stroke-width="2" fill="none"/></svg>Sed ut perspiciatis unde omnis iste</li>
    <li><svg width="13" height="13" viewBox="0 0 14 14"><circle cx="7" cy="7" r="7" fill="#9b9b9b"/><path d="M5.5 4l3 3-3 3" stroke="#fff" stroke-width="2" fill="none"/></svg>Sed ut perspiciatis unde omnis iste</li>
    <li><svg width="13" height="13" viewBox="0 0 14 14"><circle cx="7" cy="7" r="7" fill="#9b9b9b"/><path d="M5.5 4l3 3-3 3" stroke="#fff" stroke-width="2" fill="none"/></svg>Sed ut perspiciatis unde omnis iste</li>
    <li><svg width="13" height="13" viewBox="0 0 14 14"><circle cx="7" cy="7" r="7" fill="#9b9b9b"/><path d="M5.5 4l3 3-3 3" stroke="#fff" stroke-width="2" fill="none"/></svg>Sed ut perspiciatis unde omnis iste</li>
  </ul>
  <div class="btn cta">View Web Hosting Plan</div>
</div>

<!-- testimonials -->
<section class="testimonials abs" role="img" aria-label="Blue background with a faint circuit-board pattern">
  <h2 class="section-title" style="top:62px;color:#fff">CUSTOMERS <span style="color:#fff">TESTIMONIALS</span></h2>
  <div class="rule" style="left:584px;top:112px;background:#fff"></div>
  <svg class="arrow" style="left:42px" width="30" height="14" viewBox="0 0 30 14"><path d="M29 7H3M9 1L2 7l7 6" stroke="#fff" stroke-width="3" fill="none"/></svg>
  <svg class="arrow" style="left:1128px" width="30" height="14" viewBox="0 0 30 14"><path d="M1 7h26M21 1l7 6-7 6" stroke="#fff" stroke-width="3" fill="none"/></svg>

  <div class="quote" style="left:121px">
    <div class="avatar" role="img" aria-label="Customer portrait"></div>
    <div class="nbar"></div>
    <div class="name"><b>JOHN DOE ,</b> <span>Businessman</span></div>
    <p>Lorem ipsum dolor sit amet, consectetur adipiscing elit, sed eiusmod tempor incididunt ut labore et dolore magna aliqua. Ut enim ad minim veniam, quis nostrud exercitation</p>
    <div class="stars">
      <svg width="78" height="13" viewBox="0 0 78 13" fill="#f2b01e"><path id="st" d="M6.5 0l1.9 4.2 4.6.5-3.4 3.1 1 4.5-4.1-2.4-4.1 2.4 1-4.5L0 4.7l4.6-.5z"/><use href="#st" x="16"/><use href="#st" x="32"/><use href="#st" x="48"/><use href="#st" x="64"/></svg>
    </div>
  </div>
  <div class="quote" style="left:612px">
    <div class="avatar" role="img" aria-label="Customer portrait"></div>
    <div class="nbar"></div>
    <div class="name"><b>JOHN DOE ,</b> <span>Businessman</span></div>
    <p>Lorem ipsum dolor sit amet, consectetur adipiscing elit, sed eiusmod tempor incididunt ut labore et dolore magna aliqua. Ut enim ad minim veniam, quis nostrud exercitation</p>
    <div class="stars">
      <svg width="78" height="13" viewBox="0 0 78 13" fill="#f2b01e"><use href="#st"/><use href="#st" x="16"/><use href="#st" x="32"/><use href="#st" x="48"/><use href="#st" x="64"/></svg>
    </div>
  </div>
</section>

<!-- why choose us -->
<h2 class="section-title" style="top:3474px">WHY CHOOSE <span>US</span></h2>

<div class="why" style="left:107px">
  <div class="ic"><svg width="34" height="34" viewBox="0 0 34 34" fill="none" stroke="#fff" stroke-width="2.4"><rect x="7" y="4" width="18" height="24" rx="2"/><path d="M11 11h10M11 16h10M11 21h6"/><circle cx="26" cy="26" r="4" fill="#fff"/></svg></div>
  <h4>Excellent Support</h4>
  <p>Sed ut perspiciatis unde om nis iste natus error voluptatem accusantium dolorem</p>
</div>
<div class="why" style="left:356px">
  <div class="ic"><svg width="34" height="34" viewBox="0 0 34 34" fill="none" stroke="#fff" stroke-width="2.4"><rect x="6" y="4" width="18" height="25" rx="2"/><path d="M10 11h10M10 16h8M10 21h5"/><path d="M29 12L19 24l-3 1 1-3 10-12z" fill="#fff"/></svg></div>
  <h4>No Contracts</h4>
  <p>Sed ut perspiciatis unde om nis iste natus error voluptatem accusantium dolorem</p>
</div>
<div class="why" style="left:606px">
  <div class="ic"><svg width="34" height="34" viewBox="0 0 34 34" fill="none" stroke="#fff" stroke-width="2.4"><path d="M17 3l12 5v8c0 8-6 13-12 15-6-2-12-7-12-15V8z"/><circle cx="17" cy="17" r="6"/><path d="M14 17l2 2 4-4"/></svg></div>
  <h4>High Security Encryptions</h4>
  <p>Sed ut perspiciatis unde om nis iste natus error voluptatem accusantium dolorem</p>
</div>
<div class="why" style="left:855px">
  <div class="ic"><svg width="34" height="34" viewBox="0 0 34 34" fill="#fff"><ellipse cx="17" cy="8" rx="11" ry="4"/><path d="M6 11c0 2 5 4 11 4s11-2 11-4v5c0 2-5 4-11 4S6 18 6 16z"/><path d="M6 19c0 2 5 4 11 4s11-2 11-4v6c0 2-5 4-11 4S6 27 6 25z"/></svg></div>
  <h4>Unlimited Data Transfer</h4>
  <p>Sed ut perspiciatis unde om nis iste natus error voluptatem accusantium dolorem</p>
</div>

<!-- footer -->
<footer class="footer abs">
  <div class="socials abs"><i></i><i></i><i></i></div>
  <div class="contact abs">
    <div class="item"><svg width="12" height="17" viewBox="0 0 12 17"><path d="M6 0a6 6 0 0 1 6 6c0 4-6 11-6 11S0 10 0 6a6 6 0 0 1 6-6z" fill="#fff"/><circle cx="6" cy="6" r="2.3" fill="#3c3c3c"/></svg>Alderbrook, AB 40210</div>
    <div class="sep"></div>
    <div class="item"><svg width="16" height="16" viewBox="0 0 16 16"><path d="M3 0l3 4-2 2c1 2 4 5 6 6l2-2 4 3-2 3C7 16 0 9 0 2z" fill="#fff"/></svg>1 800 555 0142</div>
    <div class="sep"></div>
    <div class="item"><svg width="18" height="13" viewBox="0 0 18 13" fill="none" stroke="#fff" stroke-width="1.8"><rect x="1" y="1" width="16" height="11" rx="1"/><path d="M1 1l8 6 8-6"/></svg>info@briarloom.com</div>
  </div>
  <nav class="fmenu abs"><span>Home</span><span>About Us</span><span>Our Services</span><span>Features</span><span>Pricing</span><span>Reviews</span><span>Contact Us</span></nav>
  <div class="copy abs">© 2021 BriarLoom. All Rights Reserved</div>
</footer>

</body>
</html>
```